New web and ecommerce design for The Brindle Works

--Background--

The Brindel Works is uk biggest supplier of Coasters and coinage products. We sell mostly to the UK but have customers all around the world. We are now in need of a new website/e-commerce platform and design.

Our current site http://brindelworks.example is VERY old and outdated.

The new site should be a e-commerce site with responsive design that will look good on all handheld devices.

The customer base is both retail, b2b, and artists so it should be something that appeals to everyone and that is suitable for 2015 and forward. New and fresh.

We need a front page and one product page.

--Design--
We are looking for a new fresh design that will stand out of the crowd. We like clean and slick design that is not to cluttered. We like people and design that think a little outside the box and find new ways and design. The design should look just as good on handheld devices as on normal computers.

Some sample sites that we have been looking at

http://www.velmaronstore.example/se_en/ - We like the clean look and navigation
Attached design is also very nice (even though for a different segment)

We like nice images of live people interacting, using the products

--Competitors site--
http://www.quillbarrowglobal.example/shop-by-range/placemats-and-coasters.html To traditional but overwise nice

--Rewamp of logo--
We would also like a logo created in this. Name: The Brindel Works

--Video--
We would like to have much videos on our pages so the design must take this into account and give some samples of this.

--Handheld devices - Responsive design--
The store should look good and be adapted to work well on all handheld devices like iphone, ipad and similar android and google based systems. This is a vital part of the solution and we are looking for a solution that automatically adapts when putting in new information and images.

--PSD files--
We would like all PSD files for main page and one product page to be delivered

Target Market(s)

consumers and prestigious clients such as Harrowmere Hall and Dunstreel Court

Industry/Entity Type

Gift Shop

Number of Pages Required

2 page

Requirements
Must have
• logo
Nice to have
• clean look and feel

```html
<!DOCTYPE html>
<html lang="en">
<head>
<meta charset="utf-8">
<title>The Brindle Works</title>
<link rel="stylesheet" href="https://fonts.googleapis.com/css2?family=Mulish:wght@300;400;600;700;800&family=Open+Sans:wght@400;600&display=swap">
<style>
:root{
  --ink:#2e2e2e;
  --ink-soft:#555555;
  --muted:#7a7a7a;
  --line:#d9d9d9;
  --band:#333333;
  --hero-bg:#ececec;
  --hero-shade:#dcdcdc;
  --copy-bg:#ececec;
  --white:#ffffff;
  --video:#3a3937;
  --kin:#3b5a9a;
  --warbl:#2aa6db;
  --reel:#d8332c;
  --news:#e9862b;
}
*{box-sizing:border-box;margin:0;padding:0}
html,body{width:1200px;height:2315px;overflow:hidden;background:var(--white)}
body{position:relative;font-family:"Open Sans",Arial,sans-serif;color:var(--ink)}
.abs{position:absolute}
a{color:inherit;text-decoration:none}

/* header */
.brand{left:74px;top:20px;display:block}
.brand-name{display:block;font-family:"Mulish",sans-serif;font-weight:400;font-size:30px;line-height:34px;color:var(--ink-soft);letter-spacing:.5px}
.welcome{right:70px;top:17px;font-family:"Mulish",sans-serif;font-size:12.5px;color:var(--ink)}
.welcome b{font-weight:700}
.help{left:778px;top:64px;display:flex;gap:12px;align-items:center}
.help small{display:block;font-family:"Mulish",sans-serif;font-size:11.5px;color:var(--ink-soft)}
.help strong{display:block;font-family:"Mulish",sans-serif;font-size:15px;font-weight:700;color:var(--ink)}
.divider-v{left:945px;top:62px;width:1px;height:40px;background:var(--line)}
.cart{left:968px;top:64px;display:flex;gap:12px;align-items:center}
.cart strong{display:block;font-family:"Mulish",sans-serif;font-size:15px;font-weight:800;color:var(--ink)}
.cart small{display:block;font-family:"Mulish",sans-serif;font-size:11.5px;color:var(--ink-soft)}

/* nav */
.main-nav{left:74px;top:139px;width:1056px;height:37px;border-top:2px solid var(--ink);border-bottom:1px solid var(--ink);display:flex;align-items:stretch}
.main-nav a{font-family:"Mulish",sans-serif;font-size:12.5px;color:var(--ink);display:flex;align-items:center;justify-content:center;text-transform:uppercase;white-space:nowrap}
.main-nav a.current{background:var(--band);color:var(--white);width:230px}
.main-nav a.item{flex:1}

/* hero */
.hero{left:74px;top:195px;width:1056px;height:473px;background:linear-gradient(120deg,#f2f2f2 0%,var(--hero-bg) 45%,var(--hero-shade) 100%);overflow:hidden}
.hero-pattern{position:absolute;inset:0}
.hero-title{position:absolute;left:61px;top:108px;font-family:"Mulish",sans-serif;font-weight:400;font-size:34px;line-height:42px;color:var(--ink);text-transform:uppercase}
.hero-title b{font-weight:800}
.btn{display:inline-flex;align-items:center;justify-content:center;font-family:"Mulish",sans-serif;font-size:12px;font-weight:600;text-transform:uppercase;white-space:nowrap}
.hero-btn{position:absolute;left:61px;top:291px;width:115px;height:36px;border:2px solid var(--ink);color:var(--ink);background:var(--white)}
.hero-media{position:absolute;left:512px;top:53px;width:507px;height:362px;
  background:
    radial-gradient(ellipse 28% 45% at 88% 55%,rgba(240,176,200,.95),rgba(240,176,200,0) 100%),
    radial-gradient(ellipse 30% 40% at 58% 55%,rgba(34,46,78,.95),rgba(34,46,78,0) 100%),
    radial-gradient(ellipse 40% 55% at 28% 45%,rgba(40,48,70,.9),rgba(40,48,70,0) 100%),
    linear-gradient(135deg,#7a4524 0%,#5b3420 50%,#c9b2bb 80%,#e6e6e6 100%)}
.dots{position:absolute;left:38px;top:425px;display:flex;gap:5px}
.dots span{width:9px;height:9px;border-radius:50%;background:#9a9a9a}
.dots span:first-child{background:#555}

/* tiles */
.tile{width:334px;height:211px}
.t1{left:74px;top:697px;background:
    radial-gradient(ellipse 40% 50% at 35% 75%,rgba(50,45,40,.8),rgba(50,45,40,0)),
    radial-gradient(ellipse 45% 35% at 70% 25%,rgba(235,230,222,.9),rgba(235,230,222,0)),
    linear-gradient(160deg,#a79c8c,#5f5448 70%,#8a8070)}
.t2{left:435px;top:697px;background:#1f1f1f;display:flex;flex-direction:column;align-items:center;justify-content:center;color:var(--white);text-align:center}
.t3{left:796px;top:697px;background:
    radial-gradient(ellipse 35% 45% at 40% 65%,rgba(70,110,170,.85),rgba(70,110,170,0)),
    radial-gradient(ellipse 30% 40% at 75% 65%,rgba(60,95,150,.8),rgba(60,95,150,0)),
    linear-gradient(160deg,#f3f5f7,#c9d6e4)}
.t4{left:74px;top:936px;background:
    radial-gradient(ellipse 38% 48% at 50% 52%,rgba(70,60,40,.75),rgba(70,60,40,0)),
    radial-gradient(ellipse 20% 20% at 50% 20%,rgba(230,120,40,.8),rgba(230,120,40,0)),
    #a62324}
.t5{left:435px;top:936px;background:
    radial-gradient(ellipse 30% 35% at 25% 30%,rgba(80,140,140,.9),rgba(80,140,140,0)),
    radial-gradient(ellipse 30% 35% at 75% 70%,rgba(70,110,130,.9),rgba(70,110,130,0)),
    radial-gradient(ellipse 30% 35% at 60% 25%,rgba(210,190,140,.9),rgba(210,190,140,0)),
    linear-gradient(135deg,#d9d2c0,#a8b7a4 50%,#e4ddcc)}
.t6{left:796px;top:936px;background:
    radial-gradient(ellipse 30% 22% at 50% 22%,rgba(235,225,170,.9),rgba(235,225,170,0)),
    radial-gradient(ellipse 30% 40% at 50% 85%,rgba(215,195,180,.8),rgba(215,195,180,0)),
    linear-gradient(180deg,#f7f7f7,#dcdcdc)}
.t2 small{font-family:"Mulish",sans-serif;font-size:11px;text-transform:uppercase}
.t2 h3{font-family:"Mulish",sans-serif;font-weight:700;font-size:29px;letter-spacing:.5px;margin:2px 0 14px}
.t2 p{font-size:13.5px;line-height:21px;color:#e4e4e4}
.t2 .btn{margin-top:14px;width:98px;height:33px;border:2px solid var(--white);color:var(--white)}

/* feature heading + video */
.section-title{left:0;top:1180px;width:1200px;text-align:center;font-family:"Mulish",sans-serif;font-weight:300;font-size:35px;line-height:40px;color:var(--ink);text-transform:uppercase}
.video{left:136px;top:1287px;width:930px;height:436px;display:flex;align-items:center;justify-content:center;
  background:
    radial-gradient(ellipse 14% 30% at 18% 55%,rgba(170,150,140,.55),rgba(170,150,140,0)),
    radial-gradient(ellipse 11% 22% at 60% 55%,rgba(150,120,115,.5),rgba(150,120,115,0)),
    radial-gradient(ellipse 11% 22% at 78% 55%,rgba(70,95,120,.6),rgba(70,95,120,0)),
    var(--video)}
.intro{left:170px;top:1755px;width:860px;text-align:center;font-size:14px;line-height:24px;color:var(--ink-soft)}

/* promises */
.promises{left:74px;top:1867px;width:1056px;height:98px;border-top:1px solid var(--line);border-bottom:1px solid var(--line);display:flex}
.promise{flex:1;display:flex;align-items:center;gap:12px;padding-left:14px;border-right:1px solid var(--line)}
.promise:last-child{border-right:0}
.promise h4{font-family:"Mulish",sans-serif;font-weight:800;font-size:15px;color:var(--ink);text-transform:uppercase;white-space:nowrap}
.promise p{font-family:"Mulish",sans-serif;font-size:11.5px;color:var(--ink-soft);text-transform:uppercase;white-space:nowrap}
.price-badge{flex:none;width:40px;height:40px;border-radius:50%;background:#222;color:var(--white);font-family:"Mulish",sans-serif;font-weight:800;font-size:14px;display:flex;align-items:center;justify-content:center;margin-left:auto;margin-right:12px}

/* newsletter */
.newsletter{left:74px;top:1981px;width:810px;height:47px}
.newsletter-inner{position:absolute;inset:0;display:flex;align-items:center;gap:16px;padding-left:12px}
.newsletter h5{font-family:"Mulish",sans-serif;font-weight:700;font-size:17px;color:var(--white);text-transform:uppercase;white-space:nowrap}
.newsletter .field{width:310px;height:30px;background:var(--white);font-size:11px;color:var(--muted);display:flex;align-items:center;padding-left:8px}
.newsletter .btn{height:30px;width:104px;background:#5a5a5a;color:var(--white);border:1px solid #777}
.follow{left:890px;top:1991px;display:flex;align-items:center;gap:6px}
.follow span.label{font-family:"Mulish",sans-serif;font-weight:700;font-size:13px;color:var(--ink);margin-right:6px}
.social{width:30px;height:30px;border-radius:50%;color:var(--white);font-family:"Mulish",sans-serif;font-weight:700;font-size:14px;display:flex;align-items:center;justify-content:center}
.s-kin{background:var(--kin)}.s-warbl{background:var(--warbl)}.s-reel{background:var(--reel)}.s-news{background:var(--news)}

/* footer */
.footer-col{top:2068px;width:240px}
.footer-col h6{font-family:"Mulish",sans-serif;font-weight:700;font-size:13px;color:var(--ink);text-transform:uppercase;margin-bottom:14px}
.footer-col li{list-style:none;font-size:12px;line-height:20.6px;color:var(--ink-soft)}
.footer-rule{top:2068px;width:1px;height:160px;background:var(--line)}
.pay{display:grid;grid-template-columns:repeat(3,51px);gap:12px 6px}
.pay span{height:30px;border:1px solid #c8c8c8;background:#f7f7f7;font-family:"Open Sans",sans-serif;font-size:9px;color:var(--ink-soft);display:flex;align-items:center;justify-content:center}
.copyright{left:74px;top:2260px;width:1056px;height:37px;background:var(--copy-bg);font-size:12px;color:var(--ink-soft);display:flex;align-items:center;justify-content:center}
</style>
</head>
<body>

<header>
  <a class="brand abs" href="#">
    <span class="brand-name">The<br>Brindle Works</span>
  </a>
  <div class="welcome abs">Welcome to The Brindle Works, <b>LOGIN</b> | <b>REGISTER</b></div>

  <div class="help abs">
    <svg width="26" height="26" viewBox="0 0 24 24" aria-hidden="true"><path d="M6.6 10.8a15.2 15.2 0 0 0 6.6 6.6l2.2-2.2c.3-.3.7-.4 1-.2 1.1.4 2.3.6 3.6.6.6 0 1 .4 1 1V20c0 .6-.4 1-1 1A17 17 0 0 1 3 4c0-.6.4-1 1-1h3.5c.6 0 1 .4 1 1 0 1.3.2 2.5.6 3.6.1.3 0 .7-.2 1z" fill="#9a9a9a"/></svg>
    <div><small>Need To Help!</small><strong>01632 960418</strong></div>
  </div>
  <div class="divider-v abs"></div>
  <div class="cart abs">
    <svg width="30" height="26" viewBox="0 0 30 26" aria-hidden="true"><path d="M2 3h5l3 14h14l3-10H9" fill="none" stroke="#8a8a8a" stroke-width="2"/><circle cx="12" cy="22" r="2" fill="#8a8a8a"/><circle cx="22" cy="22" r="2" fill="#8a8a8a"/></svg>
    <div><strong>SHOPPING CART</strong><small>0 items - $0.00</small></div>
  </div>

  <nav class="main-nav abs">
    <a class="current" href="#">The Brindel Works</a>
    <a class="item" href="#">For Individuals</a>
    <a class="item" href="#">For Businesses</a>
    <a class="item" href="#">For Shops</a>
    <a class="item" href="#">For Clubs</a>
    <a class="item" href="#">For Artists</a>
    <a class="item" href="#">Contact Us</a>
  </nav>
</header>

<section class="hero abs">
  <svg class="hero-pattern" width="1056" height="473" aria-hidden="true">
    <polygon points="260,473 420,300 520,473" fill="#e2e2e2"/>
    <polygon points="420,0 620,0 500,160" fill="#e6e6e6"/>
    <polygon points="900,0 1056,0 1056,200" fill="#d4d4d4"/>
    <polygon points="950,473 1056,300 1056,473" fill="#d0d0d0"/>
  </svg>
  <h1 class="hero-title">We are a<br><b>UK manufacturer</b> of<br>a wide variety of <b>mat</b><br><b>&amp; gift products</b></h1>
  <a class="btn hero-btn" href="#">Show More</a>
  <div class="hero-media" role="img" aria-label="Framed coin and banknote collections with gift coaster cards"></div>
  <div class="dots"><span></span><span></span><span></span></div>
</section>

<section>
  <div class="tile t1 abs" role="img" aria-label="Shopfront on a town street with a cyclist passing"></div>
  <div class="tile t2 abs">
    <small>For</small>
    <h3>ARTISTS</h3>
    <p>Extend your range of products and<br>increase your profitability.</p>
    <a class="btn" href="#">Show More</a>
  </div>
  <div class="tile t3 abs" role="img" aria-label="Two colleagues working together at a laptop"></div>
  <div class="tile t4 abs" role="img" aria-label="Club crest artwork on a red background"></div>
  <div class="tile t5 abs" role="img" aria-label="Collage of printed holiday photographs"></div>
  <div class="tile t6 abs" role="img" aria-label="Child holding up a hand-drawn picture"></div>
</section>

<h2 class="section-title abs">Our special range of<br>wedding favours and mementos</h2>

<div class="video abs" role="img" aria-label="Video preview showing a coaster display stand and boxed coaster sets">
  <svg width="118" height="118" viewBox="0 0 118 118" aria-hidden="true"><circle cx="59" cy="59" r="54" fill="none" stroke="#c8c8c8" stroke-width="8"/><polygon points="47,36 84,59 47,82" fill="#c8c8c8"/></svg>
</div>

<p class="intro abs">We offer stock items as well as specialising in custom manufacture and can offer our products customised for virtually any task or occasion. The main areas we service are outlined below. However we are not 'blinkered' to these areas and are keen to offer our services to anyone who might need them. A new and different project is always something we relish.</p>

<section class="promises abs">
  <div class="promise">
    <svg width="40" height="34" viewBox="0 0 44 36" aria-hidden="true"><rect x="2" y="6" width="26" height="20" fill="none" stroke="#999" stroke-width="2"/><path d="M28 12h8l6 7v7H28z" fill="none" stroke="#999" stroke-width="2"/><circle cx="10" cy="29" r="4" fill="#fff" stroke="#999" stroke-width="2"/><circle cx="34" cy="29" r="4" fill="#fff" stroke="#999" stroke-width="2"/></svg>
    <div><h4>Free Shipping</h4><p>On over order</p></div>
    <span class="price-badge">$99</span>
  </div>
  <div class="promise">
    <svg width="40" height="40" viewBox="0 0 40 40" aria-hidden="true"><circle cx="22" cy="15" r="12" fill="none" stroke="#999" stroke-width="2"/><text x="22" y="20" text-anchor="middle" font-family="Mulish,sans-serif" font-size="13" fill="#999">$</text><path d="M2 30h10l8 4h14" fill="none" stroke="#999" stroke-width="2"/></svg>
    <div><h4>100% Money Back</h4><p>Guarantee</p></div>
  </div>
  <div class="promise">
    <svg width="40" height="40" viewBox="0 0 40 40" aria-hidden="true"><polygon points="18,3 22.5,13 33,14 25,21 27.5,32 18,26.5 8.5,32 11,21 3,14 13.5,13" fill="none" stroke="#999" stroke-width="2"/><circle cx="30" cy="31" r="7" fill="#fff" stroke="#999" stroke-width="2"/></svg>
    <div><h4>High Quality</h4><p>Products</p></div>
  </div>
  <div class="promise">
    <svg width="40" height="40" viewBox="0 0 40 40" aria-hidden="true"><path d="M4 6h32v20H18l-8 8v-8H4z" fill="#9a9a9a"/></svg>
    <div><h4>Customer Support</h4><p>We are here for you</p></div>
  </div>
</section>

<section class="newsletter abs">
  <svg width="810" height="47" style="position:absolute;inset:0" aria-hidden="true"><polygon points="0,0 810,0 790,47 0,47" fill="#333"/></svg>
  <div class="newsletter-inner">
    <svg width="24" height="18" viewBox="0 0 24 18" aria-hidden="true"><rect x="1" y="1" width="22" height="16" fill="none" stroke="#fff" stroke-width="2"/><path d="M1 1l11 9 11-9" fill="none" stroke="#fff" stroke-width="2"/></svg>
    <h5>Sign up for our newsletter!</h5>
    <span class="field">Enter Your Email Address</span>
    <span class="btn">Subscribe</span>
  </div>
</section>
<div class="follow abs">
  <span class="label">FOLLOW US :</span>
  <a class="social s-kin" href="#" aria-label="Kinlink">K</a>
  <a class="social s-warbl" href="#" aria-label="Warbl">W</a>
  <a class="social s-reel" href="#" aria-label="Reelbox">R</a>
  <a class="social s-news" href="#" aria-label="Newsline">N</a>
</div>

<footer>
  <div class="footer-col abs" style="left:74px">
    <h6>Main Navigation</h6>
    <ul><li>The Brindel Works</li><li>For Individuals</li><li>For Businesses</li><li>For Shops</li><li>For Clubs</li><li>For Artists</li><li>Contact</li></ul>
  </div>
  <div class="footer-rule abs" style="left:324px"></div>
  <div class="footer-col abs" style="left:350px">
    <h6>How can we help?</h6>
    <ul><li>My Account</li><li>Track Order</li><li>Request Quote</li><li>Delivery</li><li>Returns</li><li>Security</li></ul>
  </div>
  <div class="footer-rule abs" style="left:602px"></div>
  <div class="footer-col abs" style="left:629px">
    <h6>Company Info</h6>
    <ul><li>About Company</li><li>Careers</li><li>Terms of Use</li><li>Privacy Policy</li></ul>
  </div>
  <div class="footer-rule abs" style="left:880px"></div>
  <div class="footer-col abs" style="left:907px">
    <h6>Payment Method</h6>
    <div class="pay">
      <span>Cardwell</span><span>Paywren</span><span>Orbcard</span>
      <span>Amberline</span><span>Novapay</span>
    </div>
  </div>
  <div class="copyright abs">© 2015 Penfold Keepsakes Ltd. All Rights Reserved.</div>
</footer>

</body>
</html>
```